Business Card Design Project

Need a business card which is crisp, clear and modern.
with the logo being highlighted and at the back of the card our services.
Please use the attached logo for creating the cards.

Reason: need to receive some good designs

Target Market(s)

Our target customers will be hotels, offices, single users

Industry/Entity Type

Business

```html
<!DOCTYPE html>
<html lang="en">
<head>
<meta charset="utf-8">
<title>JoinedUp – Business Card</title>
<link rel="stylesheet" href="https://fonts.googleapis.com/css2?family=Arimo:wght@400;700&display=swap">
<style>
  :root {
    --stage: #2b2b2d;
    --paper: #f3f3f1;
    --ink: #1e1e1e;
    --ink-soft: #3a3a3a;
    --back-base: #121212;
    --green: #7cb82f;
    --magenta: #d6198a;
    --lime: #a8c23a;
    --blue: #1a9fd8;
    --orange: #e0782a;
    --yellow: #d8cf1c;
    --red: #d42a2a;
  }
  * { box-sizing: border-box; margin: 0; padding: 0; }
  html, body { width: 1200px; height: 799px; overflow: hidden; }
  body {
    background: var(--stage);
    font-family: "Arimo", Arial, sans-serif;
    color: var(--ink);
    position: relative;
  }
  .card {
    position: absolute;
    top: 245px;
    width: 530px;
    height: 310px;
    border-radius: 24px;
    overflow: hidden;
    box-shadow: 0 12px 30px rgba(0,0,0,.45);
  }
  .card--front { left: 45px; background: var(--paper); }
  .card--back { left: 625px; background: var(--back-base); }

  .colour-strip {
    position: absolute;
    left: 0; top: 0; bottom: 0;
    width: 12px;
    display: flex;
    flex-direction: column;
  }
  .colour-strip span { flex: 1; }
  .colour-strip span:nth-child(2n) { flex: .55; background: var(--paper); }
  .c-green { background: var(--green); }
  .c-magenta { background: var(--magenta); }
  .c-lime { background: var(--lime); }
  .c-blue { background: var(--blue); }
  .c-orange { background: var(--orange); }
  .c-yellow { background: var(--yellow); }

  .brand {
    position: absolute;
    left: 44px;
    top: 128px;
    display: flex;
    align-items: center;
    gap: 10px;
  }
  .brand__dot {
    width: 18px; height: 18px;
    border-radius: 50%;
    background: var(--magenta);
  }
  .brand__name {
    font-weight: 700;
    font-size: 38px;
    letter-spacing: -.5px;
    color: var(--ink);
    line-height: 1;
  }

  .divider {
    position: absolute;
    left: 262px;
    top: 70px;
    width: 1.5px;
    height: 190px;
    background: var(--ink);
  }

  .details {
    position: absolute;
    left: 276px;
    top: 70px;
  }
  .details__name { font-size: 22px; font-weight: 400; line-height: 1.1; }
  .details__role { font-size: 12px; color: var(--ink-soft); margin-top: 3px; }
  .contact { list-style: none; margin-top: 26px; font-size: 13px; line-height: 17px; }
  .contact li { display: flex; align-items: flex-start; gap: 7px; }
  .contact li + li { margin-top: 1px; }
  .contact .address { margin-bottom: 4px; }
  .contact svg { width: 12px; height: 12px; flex: none; margin-top: 2px; fill: var(--ink); }

  .back-artwork {
    position: absolute;
    inset: 0;
    background: linear-gradient(115deg,
      var(--blue) 0%,
      var(--green) 30%,
      var(--orange) 55%,
      var(--yellow) 78%,
      var(--red) 100%);
  }
</style>
</head>
<body>

<section class="card card--front" aria-label="Card front">
  <div class="colour-strip" aria-hidden="true">
    <span class="c-green"></span><span></span>
    <span class="c-magenta"></span><span></span>
    <span class="c-lime"></span><span></span>
    <span class="c-blue"></span><span></span>
    <span class="c-orange"></span><span></span>
    <span class="c-yellow"></span>
  </div>

  <div class="brand">
    <span class="brand__dot" aria-hidden="true"></span>
    <span class="brand__name">JoinedUp</span>
  </div>

  <div class="divider" aria-hidden="true"></div>

  <div class="details">
    <p class="details__name">Lennart Vosmeer</p>
    <p class="details__role">Office Manager</p>
    <ul class="contact">
      <li class="address">
        <svg viewBox="0 0 12 12" aria-hidden="true"><path d="M6 1 0.5 6h1.7v5h3V8h1.6v3h3V6h1.7z"/></svg>
        <span>Address Molenstraat 14<br>6102 KP Roerdal 000000</span>
      </li>
      <li>
        <svg viewBox="0 0 12 12" aria-hidden="true"><path d="M2.5 1h2l1 3-1.3 1a6 6 0 0 0 2.8 2.8l1-1.3 3 1v2a1.5 1.5 0 0 1-1.5 1.5A9.5 9.5 0 0 1 1 2.5 1.5 1.5 0 0 1 2.5 1z"/></svg>
        <span>+00 (0) 000 00000</span>
      </li>
      <li>
        <svg viewBox="0 0 12 12" aria-hidden="true"><path d="M3.5 0.5h5a1 1 0 0 1 1 1v9a1 1 0 0 1-1 1h-5a1 1 0 0 1-1-1v-9a1 1 0 0 1 1-1zM4 2v7h4V2z"/></svg>
        <span>+00 (0) 000 00000</span>
      </li>
      <li>
        <svg viewBox="0 0 12 12" aria-hidden="true"><path d="M3 1h6v3H3zM1 5h10v5H9V8H3v2H1zM3.5 9h5v2.5h-5z"/></svg>
        <span>+00 (0) 000 00000</span>
      </li>
      <li>
        <svg viewBox="0 0 12 12" aria-hidden="true"><path d="M0.5 2.5h11v7h-11zM1.5 3.3 6 6.6l4.5-3.3V3.2H1.5z"/></svg>
        <span>lennart@joinedup.com</span>
      </li>
      <li>
        <svg viewBox="0 0 12 12" aria-hidden="true"><path d="M6 0.5a5.5 5.5 0 1 0 0 11 5.5 5.5 0 0 0 0-11zm0 1.2c.8 0 1.6 1.6 1.8 3.6H4.2C4.4 3.3 5.2 1.7 6 1.7zm-4.2 4.8h1.3c.1 1.3.4 2.4.8 3.2a4.3 4.3 0 0 1-2.1-3.2zm0-1.2a4.3 4.3 0 0 1 2.1-3.2c-.4.8-.7 1.9-.8 3.2zm4.2 5c-.8 0-1.6-1.6-1.8-3.8h3.6c-.2 2.2-1 3.8-1.8 3.8zm2.1-.6c.4-.8.7-1.9.8-3.2h1.3a4.3 4.3 0 0 1-2.1 3.2zm.8-4.4c-.1-1.3-.4-2.4-.8-3.2a4.3 4.3 0 0 1 2.1 3.2z"/></svg>
        <span>www.joinedup.com</span>
      </li>
    </ul>
  </div>
</section>

<section class="card card--back" aria-label="Card back">
  <div class="back-artwork" role="img" aria-label="Full-bleed illustration of colourful speech bubbles on black, standing for the company's communication services"></div>
</section>

</body>
</html>
```